Downtown hair salon need trendy website

I need a website with style. Unique. We need this site to list prices , Hair and nail services, service providers hours. I would also like my logo design on the website. We are located Downtown Grand rapids. Beautiful city with lots of culture.

Target Market(s)

Men and women

Industry/Entity Type

Hair And Beauty

Coding

Coded - Design and coding required

Number of Pages Required

3 page

Font styles to use
Sans Serif

Colors

Designer to choose colors to be used in the design.

Requirements
Must have
• Logo of business. Hours, services and prices, Page for pictures of each service provider. Nail service and prices. Products that we carry... Area on page for my mission statement.
Nice to have
• Pictures of trendy of the beauty industry. Men and women cuts.. Nails..
Should not have
• booking on line options...

```html
<!DOCTYPE html>
<html lang="en">
<head>
<meta charset="utf-8">
<title>Corvane Downtown – Beauty &amp; Hair Salon</title>
<link href="https://fonts.googleapis.com/css2?family=Jost:wght@300;400;500;600;700&family=Open+Sans:ital,wght@1,400;1,600&display=swap" rel="stylesheet">
<style>
:root{
  --ink:#1a1a1a;
  --text:#333;
  --muted:#666;
  --gold:#b07a3b;
  --accent:#c0823c;
  --hero:#2b1b12;
  --sand:#f3e3c9;
  --peach:#f8dba8;
  --butter:#faeaa8;
  --white:#fff;
  --footer:#1d1d1d;
  --footer-text:#aaa;
}
*{margin:0;padding:0;box-sizing:border-box}
html,body{width:1200px;height:4285px;overflow:hidden;background:var(--white)}
body{position:relative;font-family:"Jost",sans-serif;color:var(--text)}
.abs{position:absolute}
.photo{position:absolute}
.brand{font-family:"Jost",sans-serif;font-weight:500;color:var(--gold);letter-spacing:2px;text-align:center;line-height:1}
.nav{position:absolute;top:34px;left:440px;display:flex;gap:26px;font-size:11px;color:var(--ink)}
.btn{position:absolute;display:flex;align-items:center;justify-content:center;gap:10px;font-size:8px;font-weight:600;letter-spacing:1.5px;text-transform:uppercase;white-space:nowrap}
.btn svg{width:26px;height:8px}
.btn-dark{background:var(--ink);color:var(--white)}
.btn-ghost{border:2px solid var(--white);border-radius:20px;color:var(--white)}
.btn-outline{border:2px solid var(--ink);border-radius:20px;color:var(--ink)}
.eyebrow{font-size:8px;letter-spacing:1.5px;font-weight:600;text-transform:uppercase;color:var(--muted)}
.price{color:var(--accent)}
.item-title{font-size:12px;font-weight:500;color:var(--ink)}
.item-text{font-size:10.5px;line-height:1.45;color:var(--text)}
.tile-label{position:absolute;left:60px;bottom:40px;color:var(--white)}
.tile-label .eyebrow{color:#eee}
.tile-label h3{font-size:20px;font-weight:500;white-space:nowrap}
.svc-box{position:absolute;border:2px solid var(--ink)}
.svc-box h4{position:absolute;top:-12px;left:20px;background:var(--white);padding:0 10px;font-size:14px;font-weight:500;color:var(--ink)}
.vertical{position:absolute;transform:rotate(-90deg);transform-origin:0 0;white-space:nowrap;line-height:1}
.footer h5{font-size:9px;letter-spacing:1.5px;font-weight:600;color:var(--white);text-transform:uppercase;margin-bottom:14px}
.hours{display:grid;grid-template-columns:78px auto;row-gap:8px;font-size:8.5px;letter-spacing:1px;color:var(--footer-text)}
.social{display:flex;gap:6px}
.social span{width:22px;height:22px;border:1.5px solid var(--footer-text);border-radius:50%}
</style>
</head>
<body>

<header>
  <div class="abs brand" style="left:236px;top:18px;width:100px;font-size:17px">CORVANE<div style="font-size:7px;letter-spacing:3px;margin-top:4px">DOWNTOWN</div></div>
  <nav class="nav"><span>Home</span><span>About Us</span><span>Mens</span><span>Womens</span><span>Bridal</span><span>Nails</span><span>Specials</span><span>Blogs</span><span>Contact Us</span></nav>
</header>

<section class="hero">
  <div class="abs" style="left:67px;top:73px;width:1066px;height:456px;background:var(--hero)"></div>
  <div class="photo" role="img" aria-label="Close-up portrait of a model with red lips and painted nails" style="left:700px;top:73px;width:433px;height:456px;background:linear-gradient(90deg,var(--hero),#8a6450 45%,#c9a18a)"></div>
  <div class="vertical" style="left:241px;top:402px;font-size:19px;letter-spacing:2px;color:#7a6a60;font-weight:500">corvane downtown</div>
  <div class="abs" style="left:266px;top:215px;width:2px;height:186px;background:#8a7a70"></div>
  <h1 class="abs" style="left:321px;top:208px;font-size:33px;font-weight:300;line-height:1.25;color:var(--white)">Love your nails.<br>We make your nails<br>beautiful</h1>
  <div class="btn btn-ghost" style="left:320px;top:363px;width:160px;height:28px">Book for appointment</div>
  <svg class="abs" style="left:16px;top:325px" width="24" height="16"><path d="M23 8H2M8 2L2 8l6 6" stroke="#666" stroke-width="1.5" fill="none"/></svg>
  <svg class="abs" style="left:1150px;top:325px" width="24" height="16"><path d="M1 8h21M16 2l6 6-6 6" stroke="#666" stroke-width="1.5" fill="none"/></svg>
</section>

<section class="welcome">
  <div class="abs" style="left:712px;top:529px;width:241px;height:531px;background:var(--sand)"></div>
  <div class="photo" role="img" aria-label="Stylist cutting a client's copper hair in the salon" style="left:607px;top:621px;width:500px;height:338px;background:linear-gradient(120deg,#9aa0a6,#6b5c52 50%,#c98a66)"></div>
  <h2 class="abs" style="left:243px;top:655px;width:310px;font-size:19px;font-weight:400;line-height:1.3;color:var(--ink)">Welcome to Corvane Downtown. Beauty &amp; Hair Salon. Change your look with our talented stylists.</h2>
  <p class="abs item-text" style="left:243px;top:748px;width:315px">At Corvane Downtown we are committed to providing an unparalleled experience using only the most advanced and innovative techniques to achieve classic and contemporary styles for our clients in the heart of Downtown Grand Rapids.</p>
  <div class="btn btn-dark" style="left:243px;top:864px;width:174px;height:27px">Read more about us <svg viewBox="0 0 26 8"><path d="M0 4h24M20 1l4 3-4 3" stroke="#fff" fill="none"/></svg></div>
</section>

<section class="women">
  <div class="photo" role="img" aria-label="Woman with an elegant updo seen from behind" style="left:0;top:998px;width:1200px;height:675px;background:linear-gradient(90deg,#5a4a40 0%,#8d7a6e 25%,#e6e2df 50%,#fff 62%)"></div>
  <div class="abs eyebrow" style="left:607px;top:1168px">Women haircut service</div>
  <h2 class="abs" style="left:607px;top:1190px;font-size:26px;font-weight:400;line-height:1.25;color:var(--ink)">Hairdressing with<br>a classic Design &amp; cut.</h2>
  <div class="abs" style="left:607px;top:1268px;width:58px;height:2px;background:var(--ink)"></div>
  <div class="abs" style="left:607px;top:1300px;width:340px">
    <div class="item-title">Cut/Style-Women - <span class="price">$30 &amp; Up*</span></div>
    <p class="item-text" style="margin-top:6px">Women's Haircut includes shampoo, conditioning, cut, and blow dry. Children's Haircut includes shampoo, conditioning, cut, and blow dry.</p>
    <div class="item-title" style="margin-top:20px">Styling-Blow out- <span class="price">$35 &amp; up</span></div>
    <p class="item-text" style="margin-top:2px">Shampoo &amp; Style include shampoo, conditioning, and blow out .</p>
  </div>
  <div class="btn btn-dark" style="left:607px;top:1458px;width:144px;height:27px">View details <svg viewBox="0 0 26 8"><path d="M0 4h24M20 1l4 3-4 3" stroke="#fff" fill="none"/></svg></div>
</section>

<section class="tiles">
  <div class="photo" role="img" aria-label="Barber trimming a bearded man's hair" style="left:0;top:1673px;width:300px;height:344px;background:linear-gradient(160deg,#b8b6b2,#5e4c40 60%,#2c2420)">
    <div class="tile-label"><div class="eyebrow">Hair/Beard</div><h3>Mens Service</h3></div>
  </div>
  <div class="photo" role="img" aria-label="Bridal updo with a jewelled hair accessory" style="left:300px;top:1673px;width:300px;height:344px;background:linear-gradient(160deg,#e6e0d9,#8c5a3c 55%,#5a3826)">
    <div class="tile-label" style="left:40px"><div class="eyebrow">Women Bridal</div><h3>Women Bridal Service</h3></div>
  </div>
  <div class="abs" style="left:600px;top:1673px;width:300px;height:344px;background:var(--butter)"></div>
  <div class="abs" style="left:627px;top:1733px;width:250px">
    <div class="eyebrow">Nail spa service</div>
    <h3 style="font-size:20px;font-weight:400;color:var(--ink);margin:8px 0 22px">We care for your nails</h3>
    <div class="item-title" style="font-size:11px">Shellac Manicure - <span class="price">$35</span></div>
    <div class="item-title" style="font-size:11px;margin-top:14px">Dip Powder Manicure- <span class="price">$39</span></div>
    <div class="item-title" style="font-size:11px;margin-top:14px">Classic Pedicure - <span class="price">$35</span></div>
    <p class="item-text" style="margin-top:6px;font-size:10px">The Classic Pedicure features a detoxifying foot soak that helps relax the body, clear the mind and soothe sore muscles.</p>
  </div>
  <div class="btn btn-dark" style="left:628px;top:1942px;width:144px;height:27px">View details <svg viewBox="0 0 26 8"><path d="M0 4h24M20 1l4 3-4 3" stroke="#fff" fill="none"/></svg></div>
  <div class="photo" role="img" aria-label="Model showing dark painted nails" style="left:900px;top:1673px;width:300px;height:344px;background:linear-gradient(140deg,#d9c2b0,#8a6452 50%,#3a2a22)"></div>
  <svg class="abs" style="left:899px;top:1825px" width="16" height="40"><path d="M0 0l14 20L0 40z" fill="#faeaa8"/></svg>
</section>

<section class="prices">
  <div class="svc-box" style="left:296px;top:2097px;width:291px;height:158px">
    <h4>Mens Service</h4>
    <div style="position:absolute;left:26px;top:36px;width:185px">
      <div class="item-title" style="font-size:11px">Haircut Men- <span class="price">$26 &amp; up</span></div>
      <p class="item-text" style="font-size:10px">Men's Haircut includes shampoo, conditioning, cut, and blow dry.</p>
      <div class="item-title" style="font-size:11px;margin-top:14px">Beard Trim- <span class="price">$15 &amp; Up</span></div>
    </div>
  </div>
  <div class="btn btn-dark" style="left:322px;top:2242px;width:140px;height:27px">View details <svg viewBox="0 0 26 8"><path d="M0 4h24M20 1l4 3-4 3" stroke="#fff" fill="none"/></svg></div>
  <div class="svc-box" style="left:616px;top:2097px;width:281px;height:228px">
    <h4>Bridal Service</h4>
    <div style="position:absolute;left:24px;top:36px;width:215px">
      <div class="item-title price" style="font-size:11px">Bridal Package Pricing (with Trial)</div>
      <p class="item-text" style="font-size:10px">Our package prices include a trial run appointment for both hair and makeup.</p>
      <div class="item-title" style="font-size:11px;margin-top:16px">Bridal Hair and Make-Up -<span class="price">$215</span></div>
      <p class="item-text" style="font-size:10px">Includes Trial Session with lashes</p>
      <div class="item-title" style="font-size:11px;margin-top:16px">Bridal Hair -<span class="price">$120</span></div>
      <p class="item-text" style="font-size:10px">Includes Trial Session</p>
    </div>
  </div>
  <div class="btn btn-dark" style="left:645px;top:2309px;width:140px;height:27px">View details <svg viewBox="0 0 26 8"><path d="M0 4h24M20 1l4 3-4 3" stroke="#fff" fill="none"/></svg></div>
  <p class="abs" style="left:0;top:2383px;width:1183px;text-align:center;font-family:'Open Sans',sans-serif;font-style:italic;font-size:13px;color:#888">Feel free to contact us or come visit us in downtown Grand Rapids...we are here for you!</p>
</section>

<section class="specials">
  <div class="abs" style="left:607px;top:2446px;width:593px;height:469px;background:var(--peach)"></div>
  <div class="photo" role="img" aria-label="Portrait of a woman with long wavy brown hair" style="left:0;top:2504px;width:832px;height:411px;background:linear-gradient(90deg,#6a4632,#9c6a4a 45%,#4a3022)"></div>
  <div class="abs" style="left:651px;top:2581px;width:305px;height:259px;background:#050505"></div>
  <div class="abs" style="left:691px;top:2660px;color:var(--white)">
    <div class="eyebrow" style="color:var(--accent)">Client specials</div>
    <h3 style="font-size:18px;font-weight:500;line-height:1.35;margin-top:10px">Now Offering:<br>10% discount for students</h3>
  </div>
  <div class="btn" style="left:695px;top:2750px;width:143px;height:27px;background:#222;color:var(--white)">View details <svg viewBox="0 0 26 8"><path d="M0 4h24M20 1l4 3-4 3" stroke="#fff" fill="none"/></svg></div>
  <div class="vertical" style="left:1110px;top:2900px;font-size:86px;font-weight:600;letter-spacing:3px;color:var(--white)">SPECIALS.</div>
</section>

<section class="testimonial">
  <div class="abs" role="img" aria-label="Client avatar" style="left:591px;top:2962px;width:34px;height:34px;border-radius:50%;background:#c9c4c0"></div>
  <svg class="abs" style="left:242px;top:3035px" width="18" height="10"><path d="M17 5H2M6 1L2 5l4 4" stroke="#999" fill="none"/></svg>
  <svg class="abs" style="left:940px;top:3035px" width="18" height="10"><path d="M1 5h15M12 1l4 4-4 4" stroke="#999" fill="none"/></svg>
  <p class="abs" style="left:300px;top:3027px;width:600px;text-align:center;font-family:'Open Sans',sans-serif;font-style:italic;font-size:12px;line-height:1.6;color:#444">Lorem Ipsum is simply dummy text of the printing and typesetting industry. Lorem Ipsum has been the industry's standard dummy text ever since the 1500s, when an unknown printer took a galley of type and scrambled it to make a type specimen book. It has survived not only five centuries,</p>
  <div class="abs" style="left:0;top:3124px;width:1200px;text-align:center;font-size:13px;font-weight:500;color:var(--ink)">Nora Ellison, Lansing, MI</div>
</section>

<section class="products">
  <div class="abs" style="left:268px;top:3192px;width:660px;height:282px;border:2px solid var(--ink)"></div>
  <div class="photo" role="img" aria-label="Lineup of hair care bottles and nail polish the salon carries" style="left:310px;top:3228px;width:580px;height:284px;background:linear-gradient(90deg,#eee,#f6f6f6 30%,#b07040 50%,#8a3a2a 70%,#ddd)"></div>
  <div class="vertical" style="left:950px;top:3480px;font-size:24px;font-weight:600;letter-spacing:2px;color:var(--ink)">PRODUCTS WE USE</div>
</section>

<section class="gallery">
  <div class="photo" role="img" aria-label="Blonde hair with scissors" style="left:243px;top:3578px;width:171px;height:158px;background:linear-gradient(135deg,#c9b58f,#7a6a55)"></div>
  <div class="photo" role="img" aria-label="Purple colored haircut seen from behind" style="left:424px;top:3578px;width:170px;height:158px;background:linear-gradient(135deg,#8a7a70,#5a3a6a)"></div>
  <div class="photo" role="img" aria-label="Men's fade haircut" style="left:602px;top:3578px;width:173px;height:158px;background:linear-gradient(135deg,#d6d2cc,#5a4a40)"></div>
  <div class="photo" role="img" aria-label="Short platinum hairstyle on a client" style="left:784px;top:3578px;width:171px;height:158px;background:linear-gradient(135deg,#6ab0c8,#8a5a3a)"></div>
  <div class="btn btn-outline" style="left:488px;top:3774px;width:182px;height:33px">View work gallery <svg viewBox="0 0 26 8"><path d="M0 4h24M20 1l4 3-4 3" stroke="#1a1a1a" fill="none"/></svg></div>
</section>

<footer class="footer">
  <div class="abs" style="left:0;top:3849px;width:1200px;height:436px;background:var(--footer)"></div>
  <div class="abs brand" style="left:540px;top:3906px;width:120px;font-size:17px;color:var(--white)">CORVANE<div style="font-size:7px;letter-spacing:3px;margin-top:4px">DOWNTOWN</div></div>
  <div class="abs" style="left:478px;top:4030px;width:1px;height:180px;background:#333"></div>
  <div class="abs" style="left:727px;top:4030px;width:1px;height:180px;background:#333"></div>
  <div class="abs" style="left:245px;top:4036px">
    <h5>Opening Hours</h5>
    <div class="hours">
      <span>MONDAY</span><span>10 AM-7 PM</span>
      <span>TUESDAY</span><span>9 AM-7 PM</span>
      <span>WEDNESDAY</span><span>10 AM-7 PM</span>
      <span>THURSDAY</span><span>9 AM-7 PM</span>
      <span>FRIDAY</span><span>9 AM-8 PM</span>
      <span>SATURDAY</span><span>10 AM-3 PM</span>
      <span>SUNDAY</span><span>CLOSED</span>
    </div>
  </div>
  <div class="abs" style="left:504px;top:4036px;width:210px">
    <h5>CD Blog Posts</h5>
    <div style="display:flex;gap:14px">
      <div role="img" aria-label="Blog thumbnail of a curly hairstyle" style="width:68px;height:50px;flex:none;background:linear-gradient(135deg,#5a3a2a,#9a7a6a)"></div>
      <div style="font-size:9.5px;color:var(--footer-text);line-height:1.4">Bad Hair Day Blues?<div style="font-size:8px;margin-top:6px;font-style:italic">MARCH 17, 2014</div></div>
    </div>
    <div style="display:flex;gap:14px;margin-top:12px">
      <div role="img" aria-label="Blog thumbnail of red colored hair" style="width:68px;height:50px;flex:none;background:linear-gradient(135deg,#a03a1a,#d07040)"></div>
      <div style="font-size:9.5px;color:var(--footer-text);line-height:1.4">Prolonging Your<br>Haircolor<div style="font-size:8px;margin-top:6px;font-style:italic">MARCH 17, 2014</div></div>
    </div>
    <div style="font-size:8px;letter-spacing:1px;color:var(--accent);margin-top:14px;text-decoration:underline;font-style:italic">VIEW ALL BLOG POSTS</div>
  </div>
  <div class="abs" style="left:752px;top:4036px;width:210px;font-size:8.5px;letter-spacing:1px;line-height:1.7;color:var(--footer-text)">
    <h5>Contact Details</h5>
    <div>ADDRESS: 114 LANTERN STREET N.W. #5,<br>GRAND RAPIDS, MI 49503</div>
    <div style="margin-top:12px">PHONE: 616-555-0142</div>
    <div>EMAIL: hello@corvanesalon.com</div>
    <div style="color:var(--accent);margin-top:8px;text-decoration:underline;font-style:italic">VIEW OUR LOCATION</div>
    <div class="social" style="margin-top:10px"><span></span><span></span><span></span><span></span><span></span></div>
  </div>
  <div class="abs" style="left:0;top:4235px;width:1200px;height:1px;background:#333"></div>
  <div class="abs" style="left:0;top:4258px;width:1200px;text-align:center;font-size:8px;letter-spacing:2px;color:#666">© 2019 CORVANE DOWNTOWN.</div>
</footer>

</body>
</html>
```